family chiropractic health care team needs a modern business card design

Healthcare office with Chiropractors, Physiotherapists, Massage therapists and possibly other practitioners in the future. This is a friendly family office with patients of all ages (and lots of kids) that just moved into a new larger modern office.
Look at the website for photos of the office.
Design for the front and back of a business card required.
Text for the front:
Office logo and name of the office:
Bright Path Wellness Centre
Name of current Practitioner:
Dr. Marten Quogue B.Sc., D.C. Chiropractor
(But please include options to swap out name and title for other practitioners )

address:
217 Tamsey Road
Larkhaven NR.
K2R 6P4
Phone: 416-870-2961 (MOVE)
Web site and email:
www.brightpathwellcentre.example
brightpathchiro@mailnest.example

2 versions of the back of the card:
1. text below
2. appointment schedule card

Text on back of card:
Chiropractic Card text on back of the card:
There is more to chiropractic than the relief of headaches and back pain! Our primary focus is the integrity of your nerve system, which controls and regulates every cell and tissue of your body. The moving bones of the spinal column can impair this vital communication link between your brain and body. We help improve the function and structure of your spine, reducing nerve system compromise. The result?
Even non-spinal related health problems can show improvement
without drugs
without surgery
regardless of age
for over a century
naturally

Appointment Card info For Back:
Please integrate design elements from the front of the card into an appointment card format.
M Tu W Th F Sat (and a line for writing on beside each one)

```html
<!DOCTYPE html>
<html lang="en">
<head>
<meta charset="utf-8">
<title>Bright Path Wellness Centre — Business Card</title>
<link href="https://fonts.googleapis.com/css2?family=EB+Garamond:wght@400;600&display=swap" rel="stylesheet">
<style>
  :root {
    --stage: #2b2c2e;
    --card: #ffffff;
    --card-shade: #f1f1f1;
    --green: #7cb342;
    --green-faint: #e6eedc;
    --grey: #555759;
    --grey-light: #8a8c8e;
  }
  * { box-sizing: border-box; margin: 0; padding: 0; }
  html, body {
    width: 1200px; height: 900px; overflow: hidden;
    background: var(--stage);
    font-family: "EB Garamond", Georgia, serif;
  }
  .card {
    position: absolute;
    width: 640px; height: 366px;
    background: linear-gradient(120deg, var(--card-shade) 0%, var(--card) 55%, var(--card-shade) 100%);
    box-shadow: 0 14px 30px rgba(0,0,0,.45);
    overflow: hidden;
  }
  .card--back { left: 90px; top: 60px; }
  .card--front { left: 470px; top: 480px; }

  .decor-mark {
    position: absolute; left: 40px; top: 40px;
    width: 230px; height: 230px; border-radius: 50%;
    background: var(--green-faint); opacity: .55;
  }

  .brand {
    position: absolute; right: 40px; top: 40px;
    display: flex; align-items: center; gap: 12px;
  }
  .brand__dot { width: 18px; height: 18px; border-radius: 50%; background: var(--green); }
  .brand__name {
    color: var(--green); font-weight: 600; font-size: 27px;
    letter-spacing: .5px; line-height: 1;
  }

  .message {
    position: absolute; left: 90px; right: 40px; top: 118px;
    text-align: center; color: var(--grey); font-size: 13.2px; line-height: 1.42;
  }
  .message__headline {
    color: var(--green); font-weight: 600; font-size: 16px; margin-bottom: 4px;
  }
  .message__benefits { margin-top: 6px; }
  .message__benefits span { color: var(--grey-light); padding: 0 4px; }

  .practitioner {
    position: absolute; left: 40px; right: 40px; bottom: 38px;
  }
  .practitioner__line {
    display: flex; align-items: baseline; gap: 8px;
    padding-bottom: 8px; border-bottom: 1.5px solid var(--green);
    width: 470px;
  }
  .practitioner__name { color: var(--green); font-weight: 600; font-size: 19px; letter-spacing: .3px; white-space: nowrap; }
  .practitioner__title { color: var(--grey); font-size: 16px; white-space: nowrap; }
  .practitioner__title::before { content: "| "; color: var(--green); }
  .contact { margin-top: 10px; color: var(--grey); font-size: 14px; line-height: 1.5; white-space: nowrap; }
  .contact__label { color: var(--green); }
  .contact__sep { color: var(--green); padding: 0 5px; }
</style>
</head>
<body>

<section class="card card--back" aria-label="Card back">
  <div class="decor-mark" role="img" aria-label="Faint brand decoration area"></div>
  <div class="brand">
    <span class="brand__dot"></span>
    <span class="brand__name">Bright Path Wellness Centre</span>
  </div>
  <div class="message">
    <p class="message__headline">There is more to chiropractic than the relief of headaches and back pain!</p>
    <p>Our primary focus is the integrity of your nerve system, which controls and regulates every cell and tissue of your body. The moving bones of the spinal column can impair this vital communication link between your brain and body. We help improve the function and structure of your spine, reducing nerve system compromise. The result?</p>
    <p class="message__benefits">Even non-spinal related health problems can show improvement<br>
      without drugs<span>|</span>without surgery<span>|</span>regardless of age<br>
      for over a century<span>|</span>naturally</p>
  </div>
</section>

<section class="card card--front" aria-label="Card front">
  <div class="decor-mark" role="img" aria-label="Faint brand decoration area"></div>
  <div class="brand">
    <span class="brand__dot"></span>
    <span class="brand__name">Bright Path Wellness Centre</span>
  </div>
  <div class="practitioner">
    <div class="practitioner__line">
      <span class="practitioner__name">DR. MARTEN QUOGUE B.Sc., D.C.</span>
      <span class="practitioner__title">Chiropractor</span>
    </div>
    <div class="contact">
      <p>217 Tamsey Road, Larkhaven NR. K2R 6P4<span class="contact__sep">|</span><span class="contact__label">T.</span> 416-870-2961 (MOVE)</p>
      <p><span class="contact__label">E.</span> brightpathchiro@mailnest.example<span class="contact__sep">|</span><span class="contact__label">W.</span> www.brightpathwellcentre.example</p>
    </div>
  </div>
</section>

</body>
</html>
```